LEARN Business Skills so you can Earn a good living

size of the poster is 8”x 10.75" plus 0.25" bleed.
Please leave 1 inch on the bottoum for footer
I want a design a poster that will attract people's attention.
I appreciate a creative ad however the ad should not take away from being able to clearly read the text.
-I also appreciate a simple creative ad that is not too busy.
-you can use graphics, vectors, or pictures of real people.
-however, if you use real people it should be a white male that is wearing a white shirt and look like a professional person.

Target Market(s)

Potential young business people

Industry/Entity Type

education

Requirements
Must have
• easy to read the text
Nice to have
• I would like a "creative" simple ad that is easy to be read
Should not have
• pictures of women

```html
<!DOCTYPE html>
<html lang="en">
<head>
<meta charset="utf-8">
<title>Learn IT to Earn IT – Business Enrichment Course</title>
<link href="https://fonts.googleapis.com/css2?family=Poppins:wght@600;700&family=Roboto:wght@400;500;700;900&display=swap" rel="stylesheet">
<style>
  :root {
    --paper: #f6f9fa;
    --ink: #111111;
    --text: #222222;
    --red: #c8202f;
    --gold-light: #ead9a8;
    --gold: #c9a04a;
  }
  * { margin: 0; padding: 0; box-sizing: border-box; }
  html, body {
    width: 900px; height: 1200px; overflow: hidden;
    background: var(--paper);
  }
  .poster {
    position: relative; width: 900px; height: 1200px;
    background: var(--paper);
    font-family: "Roboto", Arial, sans-serif;
    color: var(--ink);
  }
  .headline {
    position: absolute; top: 98px; left: 0; width: 100%;
    text-align: center;
    font-family: "Poppins", Arial, sans-serif;
    font-weight: 700; font-size: 77px; letter-spacing: -0.5px;
    line-height: 1;
  }
  .hero-art {
    position: absolute; top: 218px; left: 162px; width: 604px; height: 394px;
    background: linear-gradient(180deg, var(--gold-light) 0%, var(--gold) 100%);
  }
  .course-title {
    position: absolute; top: 663px; left: 0; width: 100%;
    text-align: center; color: var(--red);
    font-weight: 700; font-size: 37px; line-height: 1;
  }
  .testimonial {
    position: absolute; top: 722px; left: 150px; width: 600px; height: 90px;
  }
  .testimonial-text {
    text-align: center; font-weight: 500; font-size: 32.5px; line-height: 39px;
  }
  .quote-mark {
    position: absolute; top: 16px;
    font-family: "Roboto", Arial, sans-serif; font-weight: 900;
    font-size: 118px; line-height: 1; color: var(--red);
  }
  .quote-mark.open { left: 8px; }
  .quote-mark.close { right: 6px; }
  .skills-lead {
    position: absolute; top: 832px; left: 0; width: 100%;
    text-align: center; color: var(--red);
    font-family: "Poppins", Arial, sans-serif; font-weight: 600; font-size: 25.7px; line-height: 1;
  }
  .benefits {
    position: absolute; top: 869px; left: 0; width: 100%;
    text-align: center; font-weight: 500; font-size: 22px; line-height: 1;
  }
  .benefits .sep { margin: 0 10px; }
  .divider {
    position: absolute; top: 936px; left: 381px; width: 138px; height: 2px;
    background: var(--ink);
  }
  .topic-list {
    position: absolute; top: 981px; list-style: none;
    font-size: 16px; line-height: 19.5px; color: var(--text);
  }
  .topic-list li { position: relative; padding-left: 12px; }
  .topic-list li::before {
    content: ""; position: absolute; left: 0; top: 5px;
    width: 5px; height: 5px; border-radius: 50%; background: var(--red);
  }
  .topic-list li.continued::before { display: none; }
  .col-1 { left: 65px; }
  .col-2 { left: 327px; }
  .col-3 { left: 522px; }
  .col-4 { left: 728px; }
</style>
</head>
<body>
<main class="poster">
  <h1 class="headline">Learn IT to Earn IT</h1>

  <div class="hero-art" role="img" aria-label="Illustration of a man in a red shirt reading a tablet while sitting on a stack of gold coins"></div>

  <h2 class="course-title">Business Enrichment Course</h2>

  <div class="testimonial">
    <span class="quote-mark open">“</span>
    <p class="testimonial-text">A proven success of helping<br>people in their livelihoods</p>
    <span class="quote-mark close">”</span>
  </div>

  <p class="skills-lead">Business skills that will help you</p>
  <p class="benefits">Get A Quality Job<span class="sep">|</span>Start/grow Your Business<span class="sep">|</span>Increase Your Salary</p>

  <div class="divider"></div>

  <ul class="topic-list col-1">
    <li>Business Admnistration</li>
    <li>Small&nbsp; Business Management</li>
    <li>Finance</li>
    <li>Investments</li>
    <li>Computers</li>
    <li>Accounting</li>
  </ul>
  <ul class="topic-list col-2">
    <li>Sales</li>
    <li>Marketing</li>
    <li>Project Management</li>
    <li class="continued">Interviewing Skills</li>
    <li>Business Law</li>
    <li>Negotiation</li>
  </ul>
  <ul class="topic-list col-3">
    <li>Public Speaking</li>
    <li>Import/export</li>
    <li>Information Technoloy</li>
    <li>Distribution</li>
    <li>Marketing</li>
    <li>Ledgerly</li>
  </ul>
  <ul class="topic-list col-4">
    <li>Real Estate</li>
    <li>Health Care</li>
    <li>Management</li>
    <li>Rivermart</li>
  </ul>
</main>
</body>
</html>
```